Residential Construction Design

I'd like a business card that really explains what we do in residential construction. A big name and number, while the other information can be smaller. Since the logo is made up of grays and a teal color, the background may have to stay white? Maybe a subtle gray.(sending 2 different color schemes of the logo for different background color options) I would like a card that just appears "tough" when you look at it.

Industry/Entity Type

Residential

Contact Information for Business Card

Name and logo which will be provided.(Rex Pimbly Construction, LLC) Rex Pimbly -Licensed Contractor, Certified Home Inspector. (555) 310-7246 Email: Rpimbly_Construction@quorvane.com -Remodeling -Roofs - Siding -Drywall -Decks -Pole Barns -New Construction "Serving Southwest Michigan"

```html
<!DOCTYPE html>
<html lang="en">
<head>
<meta charset="utf-8">
<title>Rex Pimbly Construction – Business Card</title>
<link rel="stylesheet" href="https://fonts.googleapis.com/css2?family=Didact+Gothic&display=swap">
<style>
  :root {
    --backdrop: #e6e6e6;
    --card: #ffffff;
    --ink: #1a1a1a;
    --ink-soft: #5e5e5e;
    --band-dark: #1c1c1c;
    --band-mid: #9a9a9a;
    --band-text: #ffffff;
    --brand: #4a4a4a;
  }
  * { box-sizing: border-box; margin: 0; padding: 0; }
  html, body {
    width: 1200px; height: 960px; overflow: hidden;
    background: var(--backdrop);
    font-family: "Didact Gothic", "Century Gothic", sans-serif;
  }
  .business-card {
    position: absolute; left: 75px; top: 180px;
    width: 1050px; height: 600px;
    background: var(--card);
    box-shadow: 0 6px 24px rgba(0,0,0,.18);
    overflow: hidden;
  }
  .brand {
    position: absolute; top: 40px; left: 0; right: 0;
    display: flex; justify-content: center; align-items: center; gap: 18px;
  }
  .brand-mark { width: 58px; height: 58px; background: var(--brand); }
  .brand-name { font-size: 34px; color: var(--brand); }
  .owner-name, .owner-title, .owner-phone, .email {
    position: absolute; left: 0; right: 0; text-align: center;
  }
  .owner-name { top: 122px; font-size: 54px; color: var(--ink); }
  .owner-title { top: 196px; font-size: 30px; color: var(--ink-soft); }
  .owner-phone { top: 238px; font-size: 50px; color: var(--ink); }
  .service-bands { position: absolute; left: 0; top: 310px; width: 1050px; height: 220px; }
  .service-line {
    position: absolute; font-size: 30px; color: var(--band-text);
    white-space: nowrap; transform: rotate(-1.6deg); transform-origin: left center;
  }
  .service-line.primary { top: 332px; left: 175px; }
  .service-line.secondary { top: 398px; left: 30px; }
  .service-line.tertiary { top: 456px; left: 130px; }
  .email { top: 535px; font-size: 34px; color: var(--ink); }
</style>
</head>
<body>
  <main class="business-card">
    <div class="brand">
      <span class="brand-mark"></span>
      <span class="brand-name">Rex Pimbly Construction, LLC</span>
    </div>
    <h1 class="owner-name">Rex Pimbly</h1>
    <p class="owner-title">Licensed Contractor, Certified Home Inspector</p>
    <p class="owner-phone">(555) 310-7246</p>

    <svg class="service-bands" viewBox="0 0 1050 220" aria-hidden="true">
      <polygon points="0,32 1050,0 1050,66 0,92" fill="var(--band-dark)"/>
      <polygon points="0,92 1050,66 1050,92 0,152" fill="var(--band-mid)"/>
      <polygon points="0,152 1050,92 1050,170 0,212" fill="var(--band-dark)"/>
    </svg>
    <p class="service-line primary">Remodeling - Roofs - Siding - Drywall</p>
    <p class="service-line secondary">Decks - Pole Barns</p>
    <p class="service-line tertiary">New Construction "Serving Southwest Michigan"</p>

    <p class="email">Rpimbly_Construction@quorvane.com</p>
  </main>
</body>
</html>
```